Pellowfield Van Wrap Design

We are home heating specialists. We fit boilers and central heating systems as well as servicing and repairing boilers in domestic properties. We have a new logo and need our vans design to undergo some modernisation. Our vans are Short wheel base vestor piccolo.
Website www.Pellowfield-demo.co.uk
Phone 01632 960418
List of work we do:
Central heating
Installation,
Servicing,
Repairs,
Target Market(s)
Home owners and landlords
Industry/Entity Type
Gas, central heating
Other font styles liked:
- See logo fonts
Colors
0054AA
0677BA
7BADD7
CADEEF
E8F1F8
EE7325
F08F49
F5BC92
FAE3D3
FDF4ED
Requirements
Must have
- Phone number, logo, web address, Chatterloop logo, fenwry mark logo, Halverton Kreel logo, list of work we do
Nice to have
- Warm design as we are heating specialists.
Should not have
- Too much blue. Our main colour is orange.

```html
<!DOCTYPE html>
<html lang="en">
<head>
<meta charset="utf-8">
<title>Pellowfield Van Wrap</title>
<link rel="stylesheet" href="https://fonts.googleapis.com/css2?family=Montserrat:wght@500;600&family=Exo+2:ital,wght@1,800&family=Roboto:wght@500;700&family=Roboto+Condensed:wght@500&display=swap">
<style>
  :root {
    --bg: #4a4a4a;
    --orange: #ee5a24;
    --orange-rule: #ee7325;
    --blue: #0054aa;
    --blue-band: #0677ba;
    --white: #ffffff;
    --body-white: #f4f4f2;
    --glass: #c9cdcf;
    --tyre: #2b2b2b;
    --hub: #c8cacc;
    --trim: #3a3a3a;
    --badge: #f4d600;
  }
  * { margin: 0; padding: 0; box-sizing: border-box; }
  html, body { width: 1101px; height: 1200px; overflow: hidden; background: var(--bg); }
  .canvas { position: relative; width: 1101px; height: 1200px; }
  .shapes { position: absolute; inset: 0; }
  .txt { position: absolute; white-space: nowrap; }
  .brand-name { font-family: "Montserrat", sans-serif; font-weight: 500; color: var(--white); font-size: 44px; letter-spacing: 0.5px; }
  .brand-tag { font-family: "Montserrat", sans-serif; font-weight: 600; color: var(--white); font-size: 8.5px; letter-spacing: 3.4px; }
  .phone { font-family: "Roboto", sans-serif; font-weight: 700; color: var(--white); font-size: 30px; letter-spacing: 1.5px; }
  .services { font-family: "Exo 2", sans-serif; font-style: italic; font-weight: 800; color: var(--blue); font-size: 17px; list-style: none; }
  .services li { padding: 4px 0 5px; border-bottom: 1px solid var(--orange-rule); width: 160px; }
  .services li:last-child { border-bottom: none; }
  .services.flip li { text-align: right; }
  .web { font-family: "Roboto", sans-serif; font-weight: 500; color: var(--orange); font-size: 18px; }
  .social { font-family: "Roboto", sans-serif; font-weight: 700; color: var(--blue); font-size: 10px; display: flex; align-items: center; gap: 6px; }
  .social .dot { width: 14px; height: 14px; background: var(--blue-band); border-radius: 2px; }
  .partners { font-family: "Roboto", sans-serif; font-weight: 700; font-size: 12px; display: flex; gap: 18px; }
  .partners .kreel { color: #c81e1e; }
  .partners .halverton { color: var(--blue); }
  .front-name { font-family: "Montserrat", sans-serif; font-weight: 600; color: var(--orange); font-size: 19px; }
  .front-tag { font-family: "Montserrat", sans-serif; font-weight: 600; color: var(--blue); font-size: 4.5px; letter-spacing: 1.6px; }
</style>
</head>
<body>
<div class="canvas">
  <svg class="shapes" width="1101" height="1200" viewBox="0 0 1101 1200">
    <defs>
      <clipPath id="van-body">
        <path d="M130,162 Q132,148 152,148 L720,145 Q800,148 842,170 L905,215 Q958,236 964,266 L972,330 Q978,352 976,410 L975,452 L130,456 Z"/>
      </clipPath>
      <g id="van-side">
        <path d="M130,162 Q132,148 152,148 L720,145 Q800,148 842,170 L905,215 Q958,236 964,266 L972,330 Q978,352 976,410 L975,452 L130,456 Z" fill="var(--body-white)"/>
        <g clip-path="url(#van-body)">
          <polygon points="100,140 396,140 480,212 355,470 100,470" fill="var(--orange)"/>
          <polygon points="396,140 429,140 490,212 370,470 355,470 480,212" fill="var(--blue-band)"/>
          <line x1="466" y1="168" x2="466" y2="460" stroke="#dcdcda" stroke-width="1"/>
          <line x1="690" y1="168" x2="690" y2="460" stroke="#dcdcda" stroke-width="1"/>
          <rect x="100" y="430" width="900" height="40" fill="var(--trim)" opacity="0.0"/>
        </g>
        <path d="M708,205 L800,205 Q830,210 850,250 L862,292 L722,286 Z" fill="var(--glass)"/>
        <rect x="120" y="312" width="12" height="80" rx="3" fill="#b3161c"/>
        <rect x="910" y="380" width="68" height="72" rx="6" fill="var(--trim)"/>
        <rect x="118" y="425" width="40" height="32" rx="4" fill="var(--trim)"/>
        <circle cx="285" cy="450" r="54" fill="var(--bg)"/>
        <circle cx="285" cy="450" r="48" fill="var(--tyre)"/>
        <circle cx="285" cy="450" r="30" fill="var(--hub)"/>
        <circle cx="795" cy="446" r="54" fill="var(--bg)"/>
        <circle cx="795" cy="446" r="48" fill="var(--tyre)"/>
        <circle cx="795" cy="446" r="30" fill="var(--hub)"/>
        <rect x="425" y="410" width="27" height="29" fill="var(--badge)" stroke="#111" stroke-width="1.5"/>
      </g>
    </defs>
    <use href="#van-side"/>
    <g transform="translate(1101,500) scale(-1,1)">
      <use href="#van-side"/>
    </g>
  </svg>

  <!-- Driver side -->
  <div class="txt brand-name" style="left:172px; top:240px;">Pellowfield</div>
  <div class="txt brand-tag" style="left:174px; top:300px;">YOUR HOME HEATING SPECIALISTS</div>
  <div class="txt phone" style="left:172px; top:342px;">01632 960418</div>
  <ul class="txt services" style="left:500px; top:196px;">
    <li>CENTRAL HEATING</li><li>INSTALLATION</li><li>SERVICING</li><li>REPAIRS</li>
  </ul>
  <div class="txt web" style="left:478px; top:348px;">www.Pellowfield-demo.co.uk</div>
  <div class="txt social" style="left:515px; top:386px;"><span class="dot"></span>Pellowfield Heating LTD</div>
  <div class="txt partners" style="left:516px; top:420px;"><span class="kreel">KREEL</span><span class="halverton">HALVERTON</span></div>
  <div class="txt front-name" style="left:768px; top:342px;">Pellowfield</div>
  <div class="txt front-tag" style="left:769px; top:366px;">YOUR HOME HEATING SPECIALISTS</div>

  <!-- Passenger side -->
  <div class="txt brand-name" style="left:683px; top:740px;">Pellowfield</div>
  <div class="txt brand-tag" style="left:685px; top:800px;">YOUR HOME HEATING SPECIALISTS</div>
  <div class="txt phone" style="left:683px; top:842px;">01632 960418</div>
  <ul class="txt services flip" style="left:440px; top:696px;">
    <li>CENTRAL HEATING</li><li>INSTALLATION</li><li>SERVICING</li><li>REPAIRS</li>
  </ul>
  <div class="txt web" style="left:386px; top:848px;">www.Pellowfield-demo.co.uk</div>
  <div class="txt social" style="left:430px; top:886px;"><span class="dot"></span>Pellowfield Heating LTD</div>
  <div class="txt partners" style="left:432px; top:920px;"><span class="kreel">KREEL</span><span class="halverton">HALVERTON</span></div>
  <div class="txt front-name" style="left:208px; top:842px;">Pellowfield</div>
  <div class="txt front-tag" style="left:209px; top:866px;">YOUR HOME HEATING SPECIALISTS</div>
</div>
</body>
</html>
```